QM Studios needs and Interior Design Business card

I can do anything from Commercial to Residential and Free lance. Beginning to end in design selection process.
Need something to catch the eye of potential customers and vendors. From furniture to Tile and Cabinet selections. I can do it all.

Industry/Entity Type

Design Agency

Contact Information for Business Card

QM Studios- Design Consultanting Residential, Commerical
Maybe a cool detail background. Wall paper print that can have some texture

Font styles to use
Serif

Colors
709dcb
34a6d7
b868aa
e667a6
f59296
85acd3
ffffff
000000
5c5c5c

Requirements
Must have
• Square or Rectangular with Rounded edges
• Name
• Address
• Phone
• Email
Nice to have
• Some colored edges More simples not too busy
• Pattern detail in background.
Should not have
• Not too much color

```html
<!DOCTYPE html>
<html lang="en">
<head>
<meta charset="utf-8">
<title>QM Studios — Business Card</title>
<link rel="stylesheet" href="https://fonts.googleapis.com/css2?family=Jost:wght@400;500;600&display=swap">
<style>
  :root {
    --ink: #000000;
    --paper: #ffffff;
    --graphite: #5c5c5c;
    --sky: #34a6d7;
    --orchid: #b868aa;
    --rose: #e667a6;
    --backdrop: #e8e6e2;
    --card-black: #0b0b0b;
    --silver: #c9c9c9;
  }
  * { margin: 0; padding: 0; box-sizing: border-box; }
  html, body { width: 1200px; height: 802px; overflow: hidden; }
  body {
    background: var(--backdrop);
    font-family: "Jost", "Century Gothic", sans-serif;
    position: relative;
  }
  .card {
    position: absolute;
    border-radius: 34px;
    overflow: hidden;
    box-shadow: 0 6px 18px rgba(0,0,0,0.18);
  }
  /* Front */
  .card-front {
    left: 200px; top: 60px;
    width: 580px; height: 330px;
    background: var(--paper);
  }
  .front-mark {
    position: absolute;
    left: 0; top: 0;
    width: 580px; height: 330px;
  }
  .front-mark-name {
    position: absolute;
    left: 355px; top: 64px;
    width: 170px;
    text-align: center;
    font-size: 34px;
    font-weight: 500;
    line-height: 1.05;
    color: var(--ink);
  }
  .holder-name {
    position: absolute;
    left: 48px; top: 76px;
    font-size: 31px;
    color: #1a1a1a;
    font-weight: 400;
  }
  .holder-name .first { font-weight: 600; }
  .contact-list {
    position: absolute;
    left: 50px; top: 130px;
    list-style: none;
    color: #333;
  }
  .contact-list li {
    display: flex;
    align-items: center;
    gap: 6px;
    font-size: 15.5px;
    margin-bottom: 9px;
  }
  .contact-list svg { flex: none; }
  .contact-address {
    font-size: 13.5px !important;
    line-height: 1.3;
    display: block !important;
    width: 240px;
  }
  .contact-address .label { color: var(--rose); }
  .pattern-band {
    position: absolute;
    left: 0; bottom: 0;
    width: 100%; height: 62px;
    background: linear-gradient(to bottom, rgba(92,92,92,0.02), rgba(92,92,92,0.07));
  }
  /* Back */
  .card-back {
    left: 340px; top: 400px;
    width: 590px; height: 340px;
    background: linear-gradient(160deg, #1c1c1c 0%, var(--card-black) 45%, #050505 100%);
  }
  .back-circle {
    position: absolute;
    left: 250px; top: 62px;
    width: 90px; height: 90px;
    border: 3px solid var(--silver);
    border-radius: 50%;
  }
  .back-name {
    position: absolute;
    left: 0; top: 170px;
    width: 100%;
    text-align: center;
    font-size: 33px;
    font-weight: 400;
    letter-spacing: 5px;
    color: var(--silver);
  }
</style>
</head>
<body>

  <section class="card card-front">
    <svg class="front-mark" viewBox="0 0 580 330" aria-hidden="true">
      <circle cx="440" cy="82" r="120" fill="none" stroke="#1a1a1a" stroke-width="7"/>
    </svg>
    <div class="front-mark-name">QM<br>Studios</div>

    <h1 class="holder-name"><span class="first">Mateo</span> Lares</h1>

    <ul class="contact-list">
      <li class="contact-phone">
        <svg width="16" height="16" viewBox="0 0 24 24" aria-hidden="true">
          <path fill="var(--sky)" d="M6.6 10.8a15.1 15.1 0 0 0 6.6 6.6l2.2-2.2a1 1 0 0 1 1-.25 11.4 11.4 0 0 0 3.6.57 1 1 0 0 1 1 1V20a1 1 0 0 1-1 1A17 17 0 0 1 3 4a1 1 0 0 1 1-1h3.5a1 1 0 0 1 1 1c0 1.25.2 2.45.57 3.57a1 1 0 0 1-.25 1z"/>
        </svg>
        +58 (414) 555 0193
      </li>
      <li class="contact-email">
        <svg width="17" height="13" viewBox="0 0 17 13" aria-hidden="true">
          <rect x="0.75" y="0.75" width="15.5" height="11.5" fill="none" stroke="var(--orchid)" stroke-width="1.3"/>
          <path d="M1 1l7.5 6.5L16 1" fill="none" stroke="var(--orchid)" stroke-width="1.3"/>
        </svg>
        mlares@mailbox.com
      </li>
      <li class="contact-address">
        <span class="label">Address:</span> Calle 9 con avenida 4, C.C. 118 Nivel PB, Local # 3, zona Industrial Los Pinos.
      </li>
    </ul>

    <div class="pattern-band" role="img" aria-label="Faint repeating wallpaper pattern along the lower edge"></div>
  </section>

  <section class="card card-back">
    <div class="back-circle" aria-hidden="true"></div>
    <p class="back-name">QM Studios</p>
  </section>

</body>
</html>
```